Kestonvale Hawks FC Website

We are looking to develop a new website for Kestonvale FC. Kestonvale FC has now joined with Kestonvale Hawks FC and we are looking at a website that can work for both clubs. Kestonvale FC play in a local park football competition while kestonvale Hawks are a Semi Professional team that plays in the Harbourline Premier Division Competition. What we are after is two separate website off the one platform. I have attached both team logos for you to visualise. Also you can look at the existing kestonvale website www.kestonvalefc.com.au. We are looking for a huge improvement in the website and it will be imperative we have links to sponsors and the sponsors can get regular visuals. Weare looking to move this club forward and have a very professional website that can communicate clearly with the community.

Hi All,

Please remember that the website is to represent two clubs;
1. Kestonvale Hawks FC (Competes in Semi Professional League)
2. Kestonvale FC (Compete in TMCJA League which is a lower level)

Further to this the Kestonvale Hawks FC page will require a player profile page which will show photos of each player and a little bio on each.

Thanks

Reason: Would like to spend more time review existing and new designs

```html
<!DOCTYPE html>
<html lang="en">
<head>
<meta charset="utf-8">
<title>Kestonvale Hawks FC</title>
<link href="https://fonts.googleapis.com/css2?family=Arimo:wght@400;700&family=Roboto+Condensed:wght@400;700&display=swap" rel="stylesheet">
<style>
:root{
  --grass:#3f9a2a;
  --grass-light:#4aa733;
  --grass-dark:#2c7a1e;
  --footer:#2f7f22;
  --red:#d7141b;
  --red-dark:#b20f14;
  --green-text:#3c8f26;
  --ink:#333;
  --muted:#555;
  --line:#cfd8c9;
  --white:#fff;
}
*{box-sizing:border-box;margin:0;padding:0}
html,body{width:910px;height:1200px;overflow:hidden}
body{font-family:"Arimo",Arial,sans-serif;color:var(--ink);position:relative;
  background:repeating-linear-gradient(90deg,var(--grass) 0 46px,var(--grass-light) 46px 92px);}
a{color:inherit}
.abs{position:absolute}

/* header */
.club-mark{left:124px;top:12px;width:84px;height:88px}
.club-name{left:226px;top:35px;color:var(--white);font-size:21px;font-weight:700}
.club-tagline{left:226px;top:58px;color:#e7f3df;font-size:12px}
.register{left:595px;top:36px;width:108px;height:24px;background:var(--red);border:2px solid #ff4a4a;
  color:var(--white);font-size:9.5px;line-height:20px;text-align:center;text-transform:uppercase}
.social{display:flex;gap:7px}
.social span{width:20px;height:20px;border-radius:50%;background:var(--white);border:2px solid var(--red)}
.header-social{left:714px;top:38px}
.utility-nav{left:612px;top:88px;display:flex;align-items:center;gap:19px;color:var(--white);font-size:9.5px}
.main-nav{left:122px;top:114px;width:667px;height:32px;background:var(--white);padding:2px;display:flex}
.main-nav span{flex:auto;border-right:1px solid #ddd;font-size:9.5px;color:#444;text-transform:uppercase;
  display:flex;align-items:center;justify-content:center}
.main-nav span:last-child{border:none}
.main-nav .active{background:var(--red);color:var(--white)}

/* hero */
.hero{left:0;top:146px;width:910px;height:332px;
  background:linear-gradient(180deg,#c9c7b5 0%,#b1ad93 40%,#7f8a4a 70%,#5f7530 100%)}
.hero-arrow{top:295px;width:34px;height:34px;background:rgba(40,40,40,.75);border:1px solid #ddd;
  display:flex;align-items:center;justify-content:center}
.hero-caption{left:367px;top:295px;width:176px;height:33px;background:rgba(20,20,20,.85);border:1px solid #888;
  color:var(--white);font-family:"Roboto Condensed",Arial,sans-serif;font-size:16px;line-height:31px;text-align:center}

/* content */
.content{left:122px;top:478px;width:667px;height:524px;background:var(--white)}
.divider{left:405px;top:0;width:8px;height:524px;background:linear-gradient(90deg,#e8e8e8,#fff)}
.heading{font-size:18px;color:var(--green-text);font-weight:400}
.heading b{font-weight:700}
.rule{height:1px;background:var(--line)}
.bullets{list-style:none;font-size:8.6px;color:var(--muted);line-height:10.5px}
.bullets li{position:relative;padding-left:11px;margin-bottom:9px}
.bullets li::before{content:"";position:absolute;left:1px;top:4px;width:3px;height:3px;border-radius:50%;background:#666}
.btn-green{background:var(--grass-dark);color:var(--white);font-size:9px;height:16px;line-height:16px;padding:0 6px;display:inline-block}
.news-item{left:18px;width:370px;height:90px}
.news-photo{position:absolute;left:0;top:0;width:73px;height:73px;border:2px solid #ddd}
.news-title{position:absolute;left:88px;top:2px;font-size:8.8px;font-weight:700;line-height:11px;color:#222}
.news-body{position:absolute;left:88px;top:34px;font-size:8.6px;line-height:11px;color:var(--muted)}
.news-more{position:absolute;left:88px;top:66px;display:flex;align-items:center;gap:6px;font-size:8.8px;color:var(--red)}
.dot-arrow{width:13px;height:13px;border-radius:50%;background:var(--red);display:flex;align-items:center;justify-content:center}

.member{left:420px;top:28px;width:230px;height:179px;background:linear-gradient(135deg,#a80d12,#e0161d 60%,#c31118)}
.member-photo{position:absolute;left:0;top:0;width:130px;height:179px;background:linear-gradient(135deg,#8a1a1c,#c53a35);opacity:.8}
.member-text{position:absolute;right:18px;top:38px;text-align:right;color:var(--white);font-size:17px;line-height:19px;text-transform:uppercase}
.member-text b{font-size:24px;display:block;margin-top:5px}
.join{position:absolute;left:145px;top:121px;width:68px;height:20px;background:var(--white);color:var(--red);font-size:9px;font-weight:700;line-height:20px;text-align:center}

.tabs{left:420px;top:268px;width:230px;border:1px solid #b7d3a8;display:grid;grid-template-columns:86px 77px 67px;font-size:9.5px;color:#444}
.tabs span{height:22px;line-height:22px;padding-left:9px;border-right:1px solid #b7d3a8;border-bottom:1px solid #b7d3a8}
.tabs .active{background:var(--red);color:var(--white)}
.results{left:420px;top:325px;width:230px;height:122px;border:1px dashed #ccc;display:grid;grid-template-columns:1fr 1fr}
.results div{border-right:1px dashed #ccc}
.results h4{background:#ddd;font-size:9px;height:24px;line-height:24px;padding-left:13px;color:#333}
.results ul{list-style:none;padding:13px 0 0 13px;font-size:8.8px;line-height:14.5px;color:#444}

/* footer */
.footer{left:0;top:1002px;width:910px;height:114px;background:var(--footer);color:var(--white)}
.foot-col h5{font-size:9.5px;margin-bottom:9px}
.foot-col ul{list-style:none;font-size:8.6px;line-height:10.5px}
.foot-sep{width:1px;height:64px;border-left:1px dashed #6fae5e}
.sponsor{width:82px;height:38px;background:var(--white);display:flex;align-items:center;justify-content:center;
  font-size:8.5px;font-weight:700;color:#555;text-align:center;line-height:10px}
.copyright{left:0;top:1134px;width:910px;text-align:center;color:var(--white);font-size:9px;line-height:11px}
.copyright a{color:#ffdd88}
.foot-social{left:419px;top:1167px}
</style>
</head>
<body>

<header>
  <svg class="abs club-mark" viewBox="0 0 84 88" role="img" aria-label="Club crest area">
    <circle cx="42" cy="44" r="40" fill="#fff" stroke="#d7141b" stroke-width="3"/>
  </svg>
  <h1 class="abs club-name">Kestonvale Hawks FC</h1>
  <p class="abs club-tagline">The Official Website of Kestonvale Hawks FC</p>
  <div class="abs register">Register Online</div>
  <div class="abs social header-social" aria-label="Social links"><span></span><span></span><span></span></div>
  <nav class="abs utility-nav">
    <svg width="18" height="16" viewBox="0 0 18 16"><path d="M9 1 1 8h2.5v7h4v-4.5h3V15h4V8H17z" fill="#fff"/></svg>
    <span>About Us</span><span>Media</span><span>Contact Us</span>
  </nav>
  <nav class="abs main-nav">
    <span class="active">Latest News</span><span>Fixture &amp; Results</span><span>History</span><span>Profile</span>
    <span>Management</span><span>Squad</span><span>Membership</span><span>Gallery</span><span>Video</span><span>Sponsors</span>
  </nav>
</header>

<section class="abs hero" role="img" aria-label="Action photo of a striker and diving goalkeeper with the ball on a grass pitch"></section>
<div class="abs hero-arrow" style="left:36px"><svg width="12" height="18"><path d="M10 1 2 9l8 8" stroke="#fff" stroke-width="2" fill="none"/></svg></div>
<div class="abs hero-arrow" style="left:835px"><svg width="12" height="18"><path d="M2 1l8 8-8 8" stroke="#fff" stroke-width="2" fill="none"/></svg></div>
<div class="abs hero-caption">The Game Is About <b>Glory</b></div>

<main class="abs content">
  <div class="abs divider"></div>

  <h2 class="abs heading" style="left:18px;top:32px">Welcome to <b>Kestonvale Hawks FC</b></h2>
  <div class="abs rule" style="left:18px;top:60px;width:370px"></div>
  <ul class="abs bullets" style="left:18px;top:72px;width:370px">
    <li>Lorem ipsum dolor sit amet, consectetur adipisicing elit, sed do eiusmod tempor incididunt ut labore et dolore magna aliqua.</li>
    <li>Lorem ipsum dolor sit amet, consectetur adipisicing elit.</li>
    <li>Lorem ipsum dolor sit amet, consectetur adipisicing elit, sed do eiusmod tempor incididunt ut labore et dolore magna aliqua.</li>
    <li>Lorem ipsum dolor sit amet, consectetur adipisicing elit, sed do eiusmod tempor incididunt ut labore et dolore magna aliqua. Ut enim ad minim veniam, quis nostrud exercitation ullamco laboris nisi ut aliquip ex ea commodo consequat.</li>
  </ul>
  <span class="abs btn-green" style="left:18px;top:201px">Read More</span>

  <h2 class="abs heading" style="left:18px;top:242px">Top <b>News</b></h2>
  <svg class="abs" style="left:364px;top:250px" width="26" height="12"><path d="M7 1 2 6l5 5M19 1l5 5-5 5" stroke="#3c8f26" stroke-width="2" fill="none"/></svg>
  <div class="abs rule" style="left:18px;top:266px;width:370px"></div>

  <article class="abs news-item" style="top:280px">
    <div class="news-photo" role="img" aria-label="Photo of a coach in a high-visibility vest on the sideline" style="background:linear-gradient(160deg,#9fb8d0,#c98a4a 60%,#6f8f4a)"></div>
    <p class="news-title">Lorem ipsum dolor sit amet, consectetur adipisicing elit, sed do<br>eiusmod tempor incididunt ut labore et dolore magna aliqua.</p>
    <p class="news-body">Lorem Ipsum is simply dummy text of the printing and typesetting industry.<br>Lorem Ipsum has been the industry's standard dummy ....</p>
    <span class="news-more"><span class="dot-arrow"><svg width="5" height="7"><path d="M1 0l3 3.5L1 7" stroke="#fff" stroke-width="1.5" fill="none"/></svg></span><u>Read More</u></span>
  </article>
  <article class="abs news-item" style="top:383px">
    <div class="news-photo" role="img" aria-label="Photo of junior players in red kits on a field" style="background:linear-gradient(170deg,#c8d6c0,#b5473f 55%,#6d9a4a)"></div>
    <p class="news-title">Lorem ipsum dolor sit amet, consectetur adipisicing elit, sed do<br>eiusmod tempor incididunt ut labore et dolore magna aliqua.</p>
    <p class="news-body">Lorem Ipsum is simply dummy text of the printing and typesetting industry.<br>Lorem Ipsum has been the industry's standard ....</p>
    <span class="news-more"><span class="dot-arrow"><svg width="5" height="7"><path d="M1 0l3 3.5L1 7" stroke="#fff" stroke-width="1.5" fill="none"/></svg></span><u>Read More</u></span>
  </article>
  <span class="abs btn-green" style="left:18px;top:479px;padding:0 11px">View All</span>

  <aside class="abs member">
    <div class="member-photo" role="img" aria-label="Photo of a club medal and red shirt"></div>
    <p class="member-text"><b style="font-size:17px;margin:0;display:inline">Become</b><br>a Member<b>2014</b></p>
    <span class="join">JOIN NOW</span>
  </aside>

  <h2 class="abs heading" style="left:420px;top:240px">Fixutres &amp; <b>Results</b></h2>
  <div class="abs tabs">
    <span class="active">Premier League</span><span>Super League</span><span style="border-right:none">Under 16 / 2</span>
    <span style="border-bottom:none">Under 17 / 1</span><span style="border-bottom:none;grid-column:span 2;border-right:none"></span>
  </div>
  <div class="abs results">
    <div><h4>Fixture</h4><ul><li>» Under 10 / 2</li><li>» AA Men / 5</li><li>» 07 ECL / Red</li><li>» 06 / A Green</li></ul></div>
    <div style="border:none"><h4>Results</h4><ul><li>» Under 10 / 3</li><li>» AA Men / 6</li><li>» 07 ECL / Green</li><li>» 06 / B Blue</li></ul></div>
  </div>
  <span class="abs btn-green" style="left:420px;top:467px;padding:0 11px">View All</span>
</main>

<footer class="abs footer">
  <div class="abs foot-col" style="left:122px;top:22px"><h5>HOME</h5><ul><li>● <u>News</u></li><li>● Gallery</li><li>● Sponsor</li><li>● Contact Us</li></ul></div>
  <div class="abs foot-sep" style="left:198px;top:20px"></div>
  <div class="abs foot-col" style="left:225px;top:22px"><h5>PROFILE</h5><ul><li>● Management</li><li>● History</li><li>● Coach History</li><li>● Awards</li></ul></div>
  <div class="abs foot-sep" style="left:310px;top:20px"></div>
  <div class="abs foot-col" style="left:342px;top:22px"><h5>SPONSOR'S</h5></div>
  <div class="abs" style="left:739px;top:18px;display:flex;align-items:center;gap:5px;font-size:9px">
    <span class="dot-arrow" style="background:#fff"><svg width="5" height="7"><path d="M1 0l3 3.5L1 7" stroke="#d7141b" stroke-width="1.5" fill="none"/></svg></span><u>View All</u>
  </div>
  <div class="abs" style="left:342px;top:42px;display:flex;gap:9px">
    <div class="sponsor">Brightline Print</div>
    <div class="sponsor">Harlow Dunne &amp; Co</div>
    <div class="sponsor">Marlow Estates</div>
    <div class="sponsor">Northgate Trophies</div>
    <div class="sponsor">Vantrix</div>
  </div>
</footer>

<p class="abs copyright">Copyright © 2014. All Rights Reserved.<br><a href="#"><u>Privacy Policy</u></a></p>
<div class="abs social foot-social" aria-label="Social links"><span></span><span></span><span></span></div>

</body>
</html>
```